International Trading Company, 'KIRO' needs a Business Card

The company name is "KIRO" and it has own logo design.
I'd like to use its logo on this business card.
I need two side Business Card.
I'll look forward to your great design.
Thank you very much in advance.

Contact Information for Business Card

Company Name : Kiro Harbour Limited
Information Example
Dorian Pallister
Mobile(use icon please) : 1 (212) 555-0143
Tel(use icon please) : 1 (212) 555-0178
Email(use icon please) : dorian27@kiroharbour-mail.com
Address(use icon please) : 482 Halden Ave, New York, NY 10160, USA

```html
<!DOCTYPE html>
<html lang="en">
<head>
<meta charset="UTF-8">
<title>Kiro Harbour Limited – Business Card</title>
<link rel="stylesheet" href="https://fonts.googleapis.com/css2?family=Exo+2:wght@800&family=Open+Sans:wght@300;400;700&family=Saira+Condensed:wght@300&display=swap">
<style>
  :root {
    --teal: #3db999;
    --charcoal: #3e3c3d;
    --logo-grey: #58585a;
    --paper: #f3f3f5;
    --red: #ec1c24;
    --ink: #2b2b2d;
    --canvas: #ffffff;
  }
  * { margin: 0; padding: 0; box-sizing: border-box; }
  html, body { width: 1200px; height: 1200px; overflow: hidden; background: var(--canvas); }
  body { position: relative; font-family: "Open Sans", sans-serif; }

  .card {
    position: absolute;
    border-radius: 20px;
    overflow: hidden;
    background: var(--teal);
    box-shadow: 8px 10px 14px rgba(0,0,0,0.28);
  }
  .card--front { left: 182px; top: 82px; width: 838px; height: 490px; }
  .card--back  { left: 178px; top: 626px; width: 842px; height: 492px; }

  .front-curve { position: absolute; inset: 0; width: 100%; height: 100%; }

  .red-tab { position: absolute; background: var(--red); }
  .front-tab-top    { left: 393px; top: 0; width: 41px; height: 14px; }
  .front-tab-bottom { left: 308px; top: 470px; width: 279px; height: 20px; }
  .back-tab-top     { left: 390px; top: 0; width: 42px; height: 72px; }
  .back-tab-bottom  { left: 390px; top: 412px; width: 42px; height: 80px; }

  .wordmark {
    position: absolute;
    font-family: "Exo 2", sans-serif;
    font-weight: 800;
    color: var(--logo-grey);
    line-height: 1;
    letter-spacing: 4px;
    text-align: right;
  }
  .tagline {
    position: absolute;
    font-family: "Saira Condensed", sans-serif;
    font-weight: 300;
    color: var(--logo-grey);
    line-height: 1;
    text-align: right;
    white-space: nowrap;
  }
  .card--front .wordmark { right: 96px; top: 92px; font-size: 134px; }
  .card--front .tagline  { right: 120px; top: 222px; font-size: 30px; }
  .card--back .wordmark  { left: 34px; width: 295px; top: 80px; font-size: 86px; }
  .card--back .tagline   { right: 535px; top: 168px; font-size: 23px; }

  .info-panel {
    position: absolute;
    left: 410px; top: 0; right: 0; bottom: 0;
    background: var(--paper);
  }
  .back-tab-top, .back-tab-bottom { z-index: 2; }

  .holder-name {
    position: absolute;
    left: 472px; top: 40px;
    font-weight: 700;
    font-size: 36px;
    color: var(--logo-grey);
    letter-spacing: 0.5px;
    white-space: nowrap;
  }
  .contact-label {
    position: absolute;
    left: 472px; top: 94px;
    font-weight: 400;
    font-size: 27px;
    color: var(--logo-grey);
  }
  .contact-rule { position: absolute; left: 472px; top: 124px; width: 290px; height: 36px; }

  .contact-list { list-style: none; }
  .contact-item {
    position: absolute;
    left: 478px;
    display: flex;
    align-items: center;
    gap: 18px;
    font-size: 16px;
    color: var(--ink);
    white-space: nowrap;
  }
  .contact-item svg { width: 32px; height: 32px; flex: none; }
  .contact-item--phone   { top: 182px; }
  .contact-item--mobile  { top: 246px; }
  .contact-item--email   { top: 306px; }
  .contact-item--address { top: 370px; font-size: 15px; gap: 14px; }
</style>
</head>
<body>

<section class="card card--front" aria-label="Business card front">
  <svg class="front-curve" viewBox="0 0 838 490" preserveAspectRatio="none" aria-hidden="true">
    <path d="M0,10 C150,300 360,440 726,490 L0,490 Z" fill="var(--charcoal)"/>
  </svg>
  <div class="red-tab front-tab-top"></div>
  <div class="red-tab front-tab-bottom"></div>
  <div class="wordmark">KIRO</div>
  <div class="tagline">HARBOUR LIMITED</div>
</section>

<section class="card card--back" aria-label="Business card back">
  <div class="wordmark">KIRO</div>
  <div class="tagline">HARBOUR LIMITED</div>
  <div class="info-panel"></div>
  <div class="red-tab back-tab-top"></div>
  <div class="red-tab back-tab-bottom"></div>

  <h1 class="holder-name">DORIAN PALLISTER</h1>
  <div class="contact-label">contact</div>
  <svg class="contact-rule" viewBox="0 0 290 36" aria-hidden="true">
    <rect x="0" y="0" width="290" height="3" fill="var(--red)"/>
    <polygon points="224,2 266,2 245,34" fill="var(--red)"/>
  </svg>

  <ul class="contact-list">
    <li class="contact-item contact-item--phone">
      <svg viewBox="0 0 32 32" fill="none" stroke="var(--red)" stroke-width="1.8" stroke-linecap="round" stroke-linejoin="round" aria-label="Telephone">
        <path d="M7 6l4-1 3 6-3 2c1 3 4 6 7 7l2-3 6 3-1 4c-9 1-19-9-18-18z"/>
        <path d="M18 5a9 9 0 0 1 8 8M18 9a5 5 0 0 1 4 4"/>
      </svg>
      <span>1 (212) 555-0143</span>
    </li>
    <li class="contact-item contact-item--mobile">
      <svg viewBox="0 0 32 32" fill="none" stroke="var(--red)" stroke-width="1.8" aria-label="Mobile">
        <rect x="9" y="3" width="14" height="26" rx="2"/>
        <line x1="9" y1="7" x2="23" y2="7"/>
        <line x1="9" y1="24" x2="23" y2="24"/>
        <circle cx="16" cy="26.5" r="1"/>
      </svg>
      <span>1 (212) 555-0178</span>
    </li>
    <li class="contact-item contact-item--email">
      <svg viewBox="0 0 32 32" fill="none" stroke="var(--red)" stroke-width="1.8" stroke-linejoin="round" aria-label="Email">
        <rect x="3" y="8" width="26" height="17" rx="1.5"/>
        <path d="M3 9l13 10 13-10"/>
      </svg>
      <span>dorian27@kiroharbour-mail.com</span>
    </li>
    <li class="contact-item contact-item--address">
      <svg viewBox="0 0 32 32" fill="none" stroke="var(--red)" stroke-width="1.8" aria-label="Address">
        <path d="M16 30s10-10 10-17a10 10 0 0 0-20 0c0 7 10 17 10 17z"/>
        <circle cx="16" cy="13" r="3.5"/>
      </svg>
      <span>482 Halden Ave, New York, NY 10160, USA</span>
    </li>
  </ul>
</section>

</body>
</html>
```